Anzeigengestaltung für Gebäudedienstleistungsunternehmen
Zielgruppe
Wir sind ein lokales Gebäudedienstleistungsunternehmen und bieten Gebäudereinigung und Haushaltsreinigung, Grünanlagenpflege und Gartenpflege, Winterdienst und Hausmeisterservice für Privat- und Gewerbekunden an.
Aufgabenstellung
Zur Info: Wir benötigen auch ein Flyerdesign. Dieses möchten wir in Anschluss an diesen Auftrag als 1-zu-1 Projekt an den Designer unserer Anzeige vergeben.
Diese Anzeige soll in dem lokalen Mitteilungsblatt (https://www.ortsbote-velun.com/index.php) erscheinen.
Es ist eine farbige zweispaltige (92mm) Anzeige mit der Höhe von 50mm.
Unser Logo und die Firmenfarben sollen verwendet werden. Gerne darf auch ein Foto benutzt werden (z.B. im Hintergrund), welches nach den Jahreszeiten gewechselt werden kann. Zum Beispiel: Frühjahr -> Gartenpflege, Sommer -> Gebäudereinigung, Herbst -> Winterdienst und im Winter -> Hausmeisterservice.
Der Text sollte unsere Dienstleistungen enthalten. Diese sind: Gebäude- und Haushaltsreinigung, Grünanlagen- und Gartenpflege, Winterdienst und Hausmeisterservice. Zusätzlich der Hinweis, dass wir sowohl Privat als auch Gewerbekunden ansprechen möchten.
Unsere Kontaktdaten sollen auch enthalten sein:
Internet: www.brimato.de, Telefon: 09471/3582140, E-Mail: kontakt@brimato.de
Falls es noch Platz gibt, dann wäre es schön noch den lokalen Bezug herzustellen, indem man die Postleitzahl und den Ort unserer Firma nennt. Eine Nennung der Straße ist nicht vorgesehen.
PLZ: 91207 Ort: Lauf an der Pegnitz od. Lauf a.d. Pegnitz

```html
<!DOCTYPE html>
<html lang="de">
<head>
<meta charset="utf-8">
<title>Brimato Gebäudedienste – Anzeige</title>
<link rel="stylesheet" href="https://fonts.googleapis.com/css2?family=Poppins:wght@700&family=Roboto:wght@300;400;500;700&display=swap">
<style>
  :root {
    --page-top: #ffffff;
    --page-bottom: #f1f1f1;
    --ad-blue: #1f6d97;
    --ad-blue-deep: #1a5f86;
    --band-teal: #2f8fb0;
    --band-teal-light: #3aa3c2;
    --photo-teal: #2cb4c9;
    --photo-deep: #1d8fae;
    --text-white: #ffffff;
  }
  * { margin: 0; padding: 0; box-sizing: border-box; }
  html, body { width: 1166px; height: 1200px; overflow: hidden; }
  body {
    background: linear-gradient(to bottom, var(--page-top) 0, var(--page-top) 611px, var(--page-bottom) 611px);
    font-family: "Roboto", Arial, sans-serif;
    color: var(--text-white);
    position: relative;
  }
  .ad {
    position: absolute;
    left: 53px; top: 69px;
    width: 1064px; height: 578px;
    background: radial-gradient(ellipse at 40% 40%, var(--ad-blue) 0%, var(--ad-blue-deep) 100%);
    overflow: hidden;
  }
  .ad__photo {
    position: absolute;
    left: 860px; top: 0;
    width: 204px; height: 473px;
    background: linear-gradient(160deg, var(--photo-teal) 0%, var(--photo-deep) 100%);
  }
  .ad__band {
    position: absolute;
    left: 0; top: 473px;
    width: 1064px; height: 105px;
    background: linear-gradient(90deg, var(--band-teal) 0%, var(--band-teal-light) 100%);
  }
  .ad__headline {
    position: absolute;
    left: 20px; top: 14px;
    font-family: "Poppins", Arial, sans-serif;
    font-weight: 700;
    font-size: 82px;
    letter-spacing: -1px;
    line-height: 1.2;
    white-space: nowrap;
  }
  .ad__lead, .ad__audience {
    position: absolute;
    left: 21px;
    font-weight: 500;
    font-size: 27px;
    white-space: nowrap;
  }
  .ad__lead { top: 114px; }
  .ad__services {
    position: absolute;
    left: 21px; top: 150px;
    font-weight: 300;
    font-size: 27px;
    line-height: 34.3px;
  }
  .ad__audience { top: 296px; }
  .ad__cta {
    position: absolute;
    left: 21px; top: 365px;
    font-weight: 400;
    font-size: 28px;
    white-space: nowrap;
  }
  .ad__phone {
    position: absolute;
    left: 22px; top: 398px;
    font-weight: 700;
    font-size: 50px;
    letter-spacing: 0.5px;
  }
  .ad__web {
    position: absolute;
    left: 29px; top: 506px;
    font-weight: 400;
    font-size: 37px;
  }
  .brand {
    position: absolute;
    left: 600px; top: 492px;
    display: flex;
    align-items: center;
    gap: 22px;
  }
  .brand__mark {
    width: 60px; height: 60px;
    background: var(--text-white);
  }
  .brand__name {
    font-weight: 700;
    font-size: 38px;
    line-height: 38px;
    text-transform: uppercase;
    letter-spacing: 0.5px;
  }
</style>
</head>
<body>
  <section class="ad">
    <div class="ad__photo" role="img" aria-label="Foto: Mann springt kopfüber in ein türkisblaues Schwimmbecken"></div>
    <div class="ad__band"></div>

    <h1 class="ad__headline">Alles im blauen Bereich!</h1>
    <p class="ad__lead">Sie machen Urlaub, wir kümmern uns um Ihre Immobilie!</p>
    <p class="ad__services">
      Nutzen Sie unseren full-service rund um<br>
      Gebäude- und Haushaltsreinigung,<br>
      Grünanlagen- und Gartenpflege,<br>
      Winterdienst und Hausmeisterservice.
    </p>
    <p class="ad__audience">Für Privat- und Gewerbekunden!</p>
    <p class="ad__cta">FÜR WEITERE INFORMATIONEN RUFEN SIE UNS GERNE AN!</p>
    <p class="ad__phone">09471 358 2140</p>

    <p class="ad__web">www.brimato.de</p>
    <div class="brand">
      <span class="brand__mark"></span>
      <span class="brand__name">Brimato<br>Gebäudedienste</span>
    </div>
  </section>
</body>
</html>
```